Letterhead Design Project For Australian Accounting Firm

Hi All,

We need a letterhead designed for our Australian Accounting firm based in Melbourne, Victoria. I have already got a logo and business cards designed which i will add to this brief. Please design the letterhead with reference to the logo and business cards, all three items need to match. The following information needs to be included on the letterhead:

QM Advisory Logo

Suite 4 527 Harlow Street, Brunswick VIC 3056
PO Box 749, Brunswick VIC 3056

Lena Kovarik B.Com RX
Director
0491 562 804

Bartholomew Venn B.Bus RX
Director
0436 705 219

www.qmadvisory-example.com.au

at the bottom of the letterhead in small size font there needs to be the following phrase:

Liability limited by a scheme approved under Professional Standards Legislation.

Also please try and incorporate the RX logo somewhere on the letterhead

We are looking for a sharp and modern looking letterhead design, something that incorporates the look of the business card and logo.

Thanks.

```html
<!DOCTYPE html>
<html lang="en">
<head>
<meta charset="utf-8">
<title>QM Advisory Letterhead</title>
<link href="https://fonts.googleapis.com/css2?family=Open+Sans:wght@400;700&family=Arimo:wght@700&display=swap" rel="stylesheet">
<style>
  :root {
    --ink: #1a1a1a;
    --paper: #ffffff;
    --band: #1b1b1b;
    --badge-red: #c0272d;
    --frame: #8a8a8a;
  }
  html, body {
    margin: 0;
    padding: 0;
    overflow: hidden;
    background: var(--paper);
  }
  .letterhead {
    position: relative;
    width: 927px;
    height: 1200px;
    box-sizing: border-box;
    border: 1px solid var(--frame);
    background: var(--paper);
    color: var(--ink);
    font-family: "Open Sans", sans-serif;
    overflow: hidden;
  }
  .brand-name {
    position: absolute;
    left: 73px;
    top: 84px;
    width: 150px;
    margin: 0;
    font-size: 23px;
    line-height: 30px;
    font-weight: 700;
    letter-spacing: 0.2px;
    white-space: nowrap;
    color: var(--ink);
  }
  .brand-divider {
    position: absolute;
    left: 238px;
    top: 35px;
    width: 2px;
    height: 132px;
    background: var(--ink);
  }
  .services {
    position: absolute;
    left: 264px;
    top: 68px;
    margin: 0;
    font-size: 27px;
    font-weight: 400;
    line-height: 33px;
    letter-spacing: -0.3px;
    white-space: nowrap;
  }
  .accreditation {
    position: absolute;
    left: 537px;
    top: 67px;
    display: flex;
    align-items: center;
    gap: 14px;
  }
  .accreditation-text {
    font-family: "Arimo", sans-serif;
    font-weight: 700;
    font-size: 21px;
    line-height: 25px;
  }
  .address {
    position: absolute;
    left: 73px;
    top: 173px;
    margin: 0;
    font-size: 15.5px;
    line-height: 22px;
    font-style: normal;
    white-space: nowrap;
  }
  .director {
    position: absolute;
    top: 172px;
    margin: 0;
    font-size: 13px;
    line-height: 18.5px;
    white-space: nowrap;
  }
  .director--first { left: 434px; }
  .director--second { left: 605px; }
  .side-stripe {
    position: absolute;
    left: 818px;
    top: 0;
    width: 7px;
    height: 100%;
    background: var(--band);
  }
  .side-band {
    position: absolute;
    left: 840px;
    top: 0;
    width: 87px;
    height: 100%;
    background: var(--band);
  }
  .website {
    position: absolute;
    left: 873px;
    top: 24px;
    writing-mode: vertical-rl;
    transform: rotate(180deg);
    color: var(--paper);
    font-size: 18px;
    line-height: 26px;
    letter-spacing: 0.3px;
    white-space: nowrap;
  }
  .legal-note {
    position: absolute;
    left: 0;
    width: 836px;
    top: 1146px;
    margin: 0;
    text-align: center;
    font-size: 13.5px;
  }
</style>
</head>
<body>
  <main class="letterhead">
    <h1 class="brand-name">QM Advisory</h1>
    <div class="brand-divider"></div>
    <p class="services">TAXATION AND<br>BUSINESS SERVICES</p>

    <div class="accreditation">
      <svg width="68" height="68" viewBox="0 0 68 68" aria-hidden="true">
        <circle cx="34" cy="34" r="33" fill="var(--badge-red)"/>
        <circle cx="34" cy="34" r="27" fill="none" stroke="#ffffff" stroke-width="2"/>
      </svg>
      <div class="accreditation-text">Registered<br>Practitioner</div>
    </div>

    <address class="address">
      Suite 4 527 Harlow Street, Brunswick VIC 3056<br>
      PO Box 749, Brunswick VIC 3056
    </address>

    <p class="director director--first">Lena Kovarik B.Com RX<br>Director<br>0491 562 804</p>
    <p class="director director--second">Bartholomew Venn B.Bus RX<br>Director<br>0436 705 219</p>

    <div class="side-stripe"></div>
    <div class="side-band"></div>
    <div class="website">www.qmadvisory-example.com.au</div>

    <p class="legal-note">Liability limited by a scheme approved under Professional Standards Legislation.</p>
  </main>
</body>
</html>
```